Harbor Bug Guard Business Cards

A modern business card with a predominantly white background and a sleek design featuring Harbor with complimentary greys or blacks to convey a professional and contemporary look.

Front:
Primarily white background. Limited use of company purple color can be neighbored by greys.
Text: Name, Title, Cell Phone, Office Phone, Website, email address

Back:
Background Continuation: The back of the card maintains the white background for consistency.
Company name “Harbor” in company color and font, “Bug Guard” underneath or underneath left justified of “Harbor.”
A subtle pattern or texture in shades of grey to add depth behind the company Logo in font.

logo color: hex #6212ab
font: antique olive nord D Regular

```html
<!DOCTYPE html>
<html lang="en">
<head>
<meta charset="utf-8">
<title>Harbor Bug Guard Business Cards</title>
<link href="https://fonts.googleapis.com/css2?family=Archivo+Black&family=Inter:wght@400;600&display=swap" rel="stylesheet">
<style>
  :root {
    --brand: #6212ab;
    --brand-soft: #7b48b8;
    --ink: #2e2e2e;
    --ink-strong: #1a1a1a;
    --grey-light: #e6e4ea;
    --grey-faint: #f4f3f6;
    --paper: #ffffff;
    --canvas: #ecebe8;
  }
  html, body {
    margin: 0;
    padding: 0;
    width: 840px;
    height: 1200px;
    overflow: hidden;
    background: var(--canvas);
  }
  .canvas {
    position: relative;
    width: 840px;
    height: 1200px;
  }
  .card {
    position: absolute;
    left: 185px;
    width: 470px;
    height: 300px;
    background: var(--paper);
    box-shadow: 0 2px 6px rgba(0,0,0,0.12);
    overflow: hidden;
  }
  .card--back { top: 280px; }
  .card--front { top: 690px; }

  .pattern {
    position: absolute;
    left: 18px;
    top: 28px;
    width: 434px;
    height: 250px;
    background: linear-gradient(90deg, var(--grey-light) 0%, var(--grey-faint) 70%, var(--paper) 100%);
  }
  .wordmark {
    position: absolute;
    font-family: "Archivo Black", sans-serif;
    color: var(--brand);
    line-height: 1;
  }
  .wordmark__name { display: block; }
  .wordmark__tag {
    display: block;
    font-family: "Inter", sans-serif;
    font-weight: 400;
    color: var(--ink);
    letter-spacing: 2px;
    text-transform: uppercase;
  }
  .card--back .wordmark {
    right: 20px;
    top: 200px;
    background: var(--paper);
    padding: 4px 6px;
  }
  .card--back .wordmark__name { font-size: 28px; }
  .card--back .wordmark__tag { font-size: 6px; margin-top: 1px; }

  .card--front .wordmark {
    left: 22px;
    top: 132px;
  }
  .card--front .wordmark__name { font-size: 28px; }
  .card--front .wordmark__tag { font-size: 6px; margin-top: 1px; }

  .divider {
    position: absolute;
    left: 177px;
    top: 64px;
    width: 3px;
    height: 176px;
    background: var(--brand);
  }
  .divider--thin {
    left: 183px;
    top: 72px;
    width: 1px;
    height: 160px;
    background: var(--ink);
  }
  .details {
    position: absolute;
    left: 202px;
    top: 74px;
    font-family: "Inter", sans-serif;
  }
  .details__name {
    margin: 0;
    font-size: 18px;
    font-weight: 600;
    color: var(--ink);
  }
  .details__title {
    margin: 2px 0 0;
    font-size: 12px;
    color: var(--brand-soft);
  }
  .details__address {
    margin: 10px 0 14px;
    font-size: 11px;
    font-weight: 600;
    color: var(--ink-strong);
  }
  .contacts {
    list-style: none;
    margin: 0;
    padding: 0;
  }
  .contacts li {
    display: flex;
    align-items: center;
    gap: 7px;
    height: 17px;
    font-size: 11.5px;
    font-weight: 600;
    color: var(--brand);
  }
  .contacts svg {
    width: 10px;
    height: 10px;
    stroke: var(--ink);
    fill: none;
    stroke-width: 1.2;
  }
</style>
</head>
<body>
<main class="canvas">
  <section class="card card--back" aria-label="Card back">
    <div class="pattern" role="img" aria-label="Subtle grey repeated wordmark texture"></div>
    <div class="wordmark">
      <span class="wordmark__name">Harbor</span>
      <span class="wordmark__tag">Bug Guard</span>
    </div>
  </section>

  <section class="card card--front" aria-label="Card front">
    <div class="wordmark">
      <span class="wordmark__name">Harbor</span>
      <span class="wordmark__tag">Bug Guard</span>
    </div>
    <div class="divider"></div>
    <div class="details">
      <p class="details__name">Daniel J. Moore</p>
      <p class="details__title">Manager</p>
      <p class="details__address">Bayview Heights, NSW, Australia 2105</p>
      <ul class="contacts">
        <li>
          <svg viewBox="0 0 10 10"><rect x="2.5" y="0.6" width="5" height="8.8" rx="1"/><line x1="4.3" y1="8" x2="5.7" y2="8"/></svg>
          04xx xxxx xxxx
        </li>
        <li>
          <svg viewBox="0 0 10 10"><path d="M1 4 Q5 0.5 9 4 L8 5 L6.5 4 L6.5 3 Q5 2.5 3.5 3 L3.5 4 L2 5 Z"/><rect x="2" y="5.5" width="6" height="3.5" rx="0.5"/></svg>
          612-555-0148
        </li>
        <li>
          <svg viewBox="0 0 10 10"><circle cx="5" cy="5" r="4.2"/><ellipse cx="5" cy="5" rx="1.8" ry="4.2"/><line x1="0.8" y1="5" x2="9.2" y2="5"/></svg>
          harborbugguard.com
        </li>
        <li>
          <svg viewBox="0 0 10 10"><rect x="0.8" y="2" width="8.4" height="6" /><polyline points="0.8,2 5,5.5 9.2,2"/></svg>
          service@harborbugguard.com
        </li>
      </ul>
    </div>
  </section>
</main>
</body>
</html>
```